Website Design for a Luxury Wedding & Events Company

We are launching a British luxury wedding & event planning consultancy business providing bespoke, elegant and first-class service to our discerning clients in the UK and abroad. We specialize in Weddings (which will have it's on page) however we also provide service for other occasion which will be included in a single page 'Events'.

We require a company website design befitting of our luxury brand. Once designed we will post another job to code the website so that it can be hosted by HostQuill.com.

The website has to set the tone for our business and type of premium service we provide. Our website design has to be BESPOKE and have a luxury and elegant look and feel about it.

PLEASE REFER TO THE IMAGES ATTACHED TO GET AN UNDERSTANDING OF THE DESIGN CONCEPT WE WANT. ALL DESIGNS SUBMITTED MUST FOLLOW THE CONCEPT SPECIFIED!!!

We appreciate that the current budget will not permit for the design of all pages referenced above, so we are happy to have designs for up to 3 pages initially; Landing page (we have attached an examples of what we want), 'Home' page (an example is also attached) and 'About' us page. When we are happy with a particular design we can add payment for remainder of the pages required.

The final website design will have the following pages:
1a) URL Landing Page (details below)
1b) Home
2) About
3) Luxury Weddings
4) Services (this can either be a separate tab or linked to 'Luxury Weddings' - however it does need to be a separate page)
subheadings are:
> Comprehensive Wedding Planning Service
> Wedding Day Coordination Service
> Consultancy Service
5) Events
6) Gallery
7) Testimonials
8) Contact

We have a concept of the website is as follows:
URL Landing Page:
Option 1: This should just be simple but makes an immediate statement.
We have attached an image of how this could potentially look. The logo featured in the photo example needs to be replaced with our logo (reference site: http://tessawirth.com/).

Option 2: Alternatively this could be an actually door in the middle of the page - Imagine the big black gloss door at Number 7 Fenwick Terrace (London Prime Minister's home).

By clicking the door knocker on either options , the 'Home Page' will be opened.

Our tag line should also be tastefully integrated:
'Exclusive Events, Masterfully Produced, Distinctively Designed'

The 'HOME PAGE' - should look like a luxury boutique office or reception lounge (luxury table, luxury head chair and luxury 2 client chairs; elegant chandelier, beautiful flowers on the table, 2 flutes of champagne on the table; and filing cabinets with drawers that are labelled with different website pages, e.g. 'about us', 'services', 'gallery', etc. By clicking on the drawers the details behind that page will open up in a separate tab/page.)

Our tag line should be on the Home Page also.

The overall concept and look and feel of website is all about taking people on a journey and giving them a glimpse of the luxury service that awaits them.

Colours: We want the general look and feel of the website to be WHITE, or OFF-WHITE with soft hints of gold to match the logo (tab/page headings could be gold). The only dark page should be the URL Landing page (ref to website images attached).

The website and images need to be compatible with mobile devices, smartphones, iPads, etc. In terms of fit to screen, resolution etc...

We require links to our Facebook, Twitter, Instagram and Pinterest Pages (links to be provided later)

This is the rough concept and looking for designers to try to elevate this vision. :-) We are open for designers to interpret this concept in their own way.

Website wording/content is all ready to go...

We have attached our logo, and some imagery to help...

Target Market(s)

Luxury Wedding & Events Market

Industry/Entity Type

Wedding Planner

Number of Pages Required

3 page

Font styles to use
Sans Serif

Colors
ffffff

Requirements
Must have
• Tag Line:
• 'Exquisite Events, Masterfully Produced, Distinctively Designed'

```html
<!DOCTYPE html>
<html lang="en">
<head>
<meta charset="utf-8">
<title>Elena Marlowe – Luxury Wedding &amp; Event Consultants</title>
<link rel="stylesheet" href="https://fonts.googleapis.com/css2?family=Maven+Pro:wght@500&family=PT+Sans:wght@400&display=swap">
<style>
  :root {
    --ink: #111111;
    --gold: #c59446;
    --gold-light: #f7d98a;
    --gold-text: #e6c46a;
    --nav-text: #f2f2f2;
    --footer-text: #cfcfcf;
    --caption-bg: rgba(255, 255, 255, 0.82);
    --caption-text: #151515;
    --rule: #4a4a4a;
  }
  * { box-sizing: border-box; margin: 0; padding: 0; }
  html, body {
    width: 1200px; height: 985px; overflow: hidden;
    background: var(--ink);
    font-family: "PT Sans", sans-serif;
  }
  .page { position: relative; width: 1200px; height: 985px; }

  .site-header {
    height: 137px;
    display: flex; flex-direction: column; align-items: center; justify-content: center;
    border-bottom: 2px dotted var(--rule);
  }
  .brand { display: flex; flex-direction: column; align-items: center; gap: 6px; }
  .brand-mark {
    width: 54px; height: 54px; border-radius: 50%;
    border: 2px solid var(--gold);
  }
  .brand-name {
    color: var(--gold-text);
    font-size: 19px; letter-spacing: 3px;
  }
  .brand-tagline {
    color: var(--gold-text);
    font-size: 7px; letter-spacing: 1px; margin-top: -4px;
  }

  .main-nav {
    height: 54px;
    display: flex; align-items: center; justify-content: center; gap: 26px;
    font-size: 13px; letter-spacing: 0.3px;
  }
  .main-nav a { color: var(--nav-text); text-decoration: none; }
  .main-nav a.is-active { color: var(--gold-text); }
  .nav-sep { width: 7px; height: 7px; border-radius: 50%; background: var(--gold); opacity: 0.7; }

  .hero {
    position: absolute; left: 0; top: 191px; width: 1200px; height: 618px;
    background:
      radial-gradient(ellipse 180px 160px at 640px 260px, #d9a9ae 0%, rgba(217,169,174,0) 100%),
      radial-gradient(ellipse 220px 260px at 990px 460px, #2a2a2a 0%, rgba(42,42,42,0) 70%),
      radial-gradient(ellipse 260px 200px at 1050px 120px, #6d7b52 0%, rgba(109,123,82,0) 100%),
      radial-gradient(ellipse 260px 340px at 410px 320px, #f1efea 0%, rgba(241,239,234,0) 100%),
      linear-gradient(180deg, #e9e4dc 0%, #d6cdc0 55%, #9a8870 100%);
  }
  .hero-arrow {
    position: absolute; top: 289px; width: 40px; height: 40px;
  }
  .hero-arrow.prev { left: 20px; }
  .hero-arrow.next { right: 25px; }

  .hero-caption {
    position: absolute; left: 111px; top: 402px; width: 797px; height: 161px;
    background: var(--caption-bg);
    padding: 34px 0 0 53px;
    font-family: "Maven Pro", sans-serif;
    font-size: 38px; line-height: 52px; letter-spacing: 0.8px;
    color: var(--caption-text);
    text-transform: uppercase;
  }

  .social-band {
    position: absolute; left: 0; top: 809px; width: 1200px; height: 97px;
    background: var(--gold);
    display: flex; align-items: center; justify-content: center; gap: 9px;
  }
  .social-link {
    width: 43px; height: 43px; border-radius: 50%;
    background: var(--gold-light);
    display: block;
  }

  .site-footer {
    position: absolute; left: 0; top: 906px; width: 1200px; height: 79px;
    display: flex; align-items: center; justify-content: center;
    font-size: 12px; color: var(--footer-text);
  }
  .site-footer .brand-link { color: var(--gold-text); }
</style>
</head>
<body>
<div class="page">
  <header class="site-header">
    <div class="brand">
      <span class="brand-mark"></span>
      <span class="brand-name">ELENA MARLOWE</span>
      <span class="brand-tagline">LUXURY WEDDING &amp; EVENT CONSULTANTS</span>
    </div>
  </header>

  <nav class="main-nav">
    <a href="#" class="is-active">HOME</a><span class="nav-sep"></span>
    <a href="#">ABOUT</a><span class="nav-sep"></span>
    <a href="#">LUXURY WEDDINGS</a><span class="nav-sep"></span>
    <a href="#">SERVICES</a><span class="nav-sep"></span>
    <a href="#">EVENTS</a><span class="nav-sep"></span>
    <a href="#">GALLERY</a><span class="nav-sep"></span>
    <a href="#">TESTIMONIALS</a><span class="nav-sep"></span>
    <a href="#">CONTACT</a>
  </nav>

  <section class="hero" role="img" aria-label="Photo of a wedding table with a crystal glass, pink roses, baby's breath in a white jug and a chalkboard table number">
    <svg class="hero-arrow prev" viewBox="0 0 40 40" aria-hidden="true">
      <circle cx="20" cy="20" r="18" fill="rgba(255,255,255,0.6)" stroke="#9a9a9a" stroke-width="2.5"/>
      <path d="M24 12 L14 20 L24 28 Z" fill="#8a8a8a"/>
    </svg>
    <svg class="hero-arrow next" viewBox="0 0 40 40" aria-hidden="true">
      <circle cx="20" cy="20" r="18" fill="rgba(255,255,255,0.6)" stroke="#9a9a9a" stroke-width="2.5"/>
      <path d="M16 12 L26 20 L16 28 Z" fill="#8a8a8a"/>
    </svg>
    <h1 class="hero-caption">Exclusive events, masterfully<br>produced, distinctively designed</h1>
  </section>

  <div class="social-band">
    <a class="social-link" href="#" aria-label="Social page 1"></a>
    <a class="social-link" href="#" aria-label="Social page 2"></a>
    <a class="social-link" href="#" aria-label="Social page 3"></a>
    <a class="social-link" href="#" aria-label="Social page 4"></a>
  </div>

  <footer class="site-footer">
    <p>Copyrights @ 2015&nbsp;<span class="brand-link">Elena Marlowe.</span>&nbsp;All Rights Reserved.</p>
  </footer>
</div>
</body>
</html>
```